NEW Website DESIGN for Brightwell Panes & Stoneworks Company

Brand New website, contemporary, clean, visual (images), not busy. ATTACHED IS OUR LOG THAT YOU MUST USE.

The company is called Brightwell Panes & Stoneworks (BrightwellPS)
www.brightwellps.com
The website should be www.brightwellpns.com
one page for glass one page for solid surfaces www.brightwellpanesplashes.co.uk
www.brightwellstoneworkss.co.uk

Target Market(s)

Hotels, Commercial projects, Small focus on residential

Industry/Entity Type

Construction

Number of Pages Required

5+ page

Font styles to use
Sans Serif

Requirements
Must have
• COLOURS AS PER OUR LOGO - WHITE/YELLOW/GREY - WHITE BACK GROUND
• CLEAR SIMPLE NAVIGATION - MODER CLEAN CUT - DESIGN FEEL
• LATEST NAVIGATION FOR IMAGES and text to include per project details
• WORK/PROJECT AREA - NEWS AREA - TEAM AREA/ABOUT US/CONTACT US
• NEW PAGEwww.brightwellpanesplashes.co.uk - NEW PAGE www.brightwellstoneworkss.co.uk
• PLEASE COPY THIS TYPE OF TEMPALTE
• https://www.harlowmead.co.uk/project/grand-halls/
• MOBILE READY
• WORDPRESS
• MODERN IMAGES INCLUDING VELMARA KESTRIN AND GLASS PROJECTS
Nice to have
• NEW DESIGN MODER FRESH
• WEBSITES I LIKE THE TEMPLATE SHOULD BE LIKE THE WEBSITE BELOW
• https://www.harlowmead.co.uk/
Should not have
• NOT Old fashion template, not busy NAVIGATION
• NO BLACK
• NO DARK GREYS
• NOT LOTS OF YELLOW
• RESDENTIAL IMAGES

```html
<!DOCTYPE html>
<html lang="en">
<head>
<meta charset="utf-8">
<title>Brightwell Panes &amp; Stoneworks</title>
<link rel="stylesheet" href="https://fonts.googleapis.com/css2?family=Roboto:wght@300;400;500;700&display=swap">
<style>
:root{
  --teal:#1b8a9b;
  --text:#555a5c;
  --heading:#4a4f52;
  --muted:#8a8f91;
  --white:#ffffff;
  --band:#f3f4f3;
  --line:#8fcbd3;
}
*{margin:0;padding:0;box-sizing:border-box}
html,body{width:1200px;height:2212px;overflow:hidden;background:var(--white)}
body{position:relative;font-family:"Roboto",Arial,sans-serif;color:var(--text)}
.abs{position:absolute}

/* sidebar */
.sidebar{left:0;top:0;width:74px;height:2212px;border-right:1px solid var(--line);background:var(--white);z-index:5}
.menu-icon{left:20px;top:22px}
.side-brand{left:2px;top:68px;width:70px;text-align:center;font-size:8px;font-weight:500;color:var(--muted);white-space:nowrap}
.side-brand .dot{display:block;width:48px;height:48px;border-radius:50%;background:var(--muted);margin:0 auto 3px}
.side-link{left:37px;transform:translate(-50%,-50%) rotate(-90deg);white-space:nowrap;font-size:18px;color:var(--muted);letter-spacing:.5px;padding-left:10px}
.side-link::before{content:"";position:absolute;left:0;top:4px;width:2px;height:16px;background:var(--teal)}

/* hero */
.hero{left:74px;top:0;width:1126px;height:675px}
.hero-glass{left:0;top:0;width:563px;height:675px;background:linear-gradient(180deg,#eceeee 0%,#e2e5e5 35%,#f0f0ef 60%,#e6e6e5 82%,#b98555 90%,#a8743f 100%)}
.hero-solid{left:563px;top:0;width:563px;height:675px;background:linear-gradient(135deg,#4b3626 0%,#6d5036 35%,#3c2c20 60%,#5a4330 100%)}
.hero-logo{left:363px;top:70px;width:400px;text-align:center;color:var(--white);font-size:17px;font-weight:500;white-space:nowrap}
.hero-logo .dot{display:block;width:92px;height:92px;border-radius:50%;background:var(--white);margin:0 auto 14px}
.cat-btn{display:flex;align-items:center;justify-content:center;text-align:center;width:187px;height:149px;font-size:30px;font-weight:400;line-height:1.4}
.cat-glass{left:190px;top:463px;background:var(--white);color:var(--heading)}
.cat-solid{left:751px;top:463px;border:1px solid rgba(255,255,255,.85);color:var(--white)}

/* feature */
.stack-back{left:137px;top:737px;width:300px;height:439px;background:linear-gradient(90deg,#d9dcdc,#f4f4f3)}
.stack-mid{left:170px;top:768px;width:436px;height:438px;background:linear-gradient(180deg,#f1f1f0,#cfd0cf)}
.stack-front{left:201px;top:800px;width:436px;height:436px;background:linear-gradient(160deg,#5e5f60 0%,#d9d7d1 35%,#e6e4df 60%,#6b6c6d 100%);box-shadow:0 0 0 1px #fff}
.pager{top:1258px;width:31px;height:31px;display:flex;align-items:center;justify-content:center}
.pager-prev{left:381px;border:1px solid var(--teal)}
.pager-next{left:427px;background:var(--teal)}
.feature-title{left:700px;top:852px;font-size:38px;font-weight:700;letter-spacing:3px;color:var(--heading)}
.feature-sub{left:700px;top:907px;font-size:28px;font-weight:400;color:var(--heading)}
.feature-sub::before{content:"";position:absolute;left:0;top:-6px;width:22px;height:2px;background:var(--teal)}
.feature-text{left:700px;top:950px;width:352px;font-size:12.6px;line-height:22.3px;color:var(--text)}
.btn-more{left:700px;top:1160px;width:88px;height:25px;border:1px solid var(--teal);color:var(--teal);font-size:12px;display:flex;align-items:center;justify-content:center}

/* about band */
.about{left:75px;top:1349px;width:1125px;height:676px;background:var(--band)}
.about-title{font-size:27px;font-weight:400;color:var(--heading)}
.about-title::after{content:"";position:absolute;left:0;bottom:-3px;width:22px;height:2px;background:var(--teal)}
.office-title{left:149px;top:1408px}
.office-text{left:149px;top:1447px;width:430px;font-size:12.6px;line-height:22.3px}
.office-text p+p{margin-top:14px}
.office-text a{color:#2a5bd7;text-decoration:underline}
.office-photo{left:637px;top:1413px;width:301px;height:186px;background:linear-gradient(180deg,#4f7a3c 0%,#2f4e68 40%,#5d8d45 70%,#a7b86f 100%)}
.map{left:399px;top:1599px;width:238px;height:362px;background:linear-gradient(160deg,#ffffff 0%,#2f7fc1 30%,#e0126f 65%,#ffffff 100%)}
.coverage-title{left:698px;top:1658px}
.coverage-text{left:698px;top:1697px;width:362px;font-size:12.6px;line-height:22.3px}
.coverage-text p+p{margin-top:14px}

/* footer */
.footer{left:75px;top:2025px;width:1125px;height:187px;border-top:1px solid var(--line)}
.foot-label{font-size:15px;font-weight:500;letter-spacing:1.5px;color:var(--heading)}
.follow-label{left:149px;top:2066px}
.social{left:149px;top:2098px;display:flex;gap:3px}
.social span{width:26px;height:26px;border-radius:50%}
.social .s1{background:#dd4b39}.social .s2{background:#3b5998}.social .s3{background:#f2862e}.social .s4{background:#4aa8e6}
.follow-rule{left:149px;top:2167px;width:113px;height:1px;background:var(--line)}
.legal{left:149px;top:2183px;font-size:10.5px;color:var(--text)}
.legal .sep{margin:0 12px}
.foot-divider{left:436px;top:2068px;width:1px;height:100px;background:var(--line)}
.contact-label{left:467px;top:2066px}
.contact-row{left:467px;display:flex;align-items:center;gap:22px;font-size:13px;color:var(--teal)}
.row-phone{top:2100px}
.row-mail{top:2140px}
.copyright{left:467px;top:2183px;font-size:10.5px;color:var(--text)}
.foot-brand{left:820px;top:2055px;width:262px;text-align:center;color:var(--muted);font-size:16px;font-weight:500;white-space:nowrap}
.foot-brand .dot{display:block;width:92px;height:92px;border-radius:50%;background:var(--muted);margin:0 auto 14px}
</style>
</head>
<body>

<aside class="abs sidebar">
  <svg class="abs menu-icon" width="34" height="24" viewBox="0 0 34 24"><g stroke="#1b8a9b" stroke-width="3"><line x1="0" y1="2" x2="34" y2="2"/><line x1="0" y1="12" x2="34" y2="12"/><line x1="0" y1="22" x2="34" y2="22"/></g></svg>
  <div class="abs side-brand"><span class="dot"></span>BrightwellPS</div>
  <div class="abs side-link" style="top:338px">Categories</div>
  <div class="abs side-link" style="top:1015px">Projects</div>
  <div class="abs side-link" style="top:1690px">About Us</div>
</aside>

<section class="abs hero">
  <div class="abs hero-glass" role="img" aria-label="White kitchen with turquoise glass splashback"></div>
  <div class="abs hero-solid" role="img" aria-label="Bathroom with dark stone wall and white solid surface basin"></div>
  <div class="abs hero-logo"><span class="dot"></span>Brightwell Panes &amp; Stoneworks</div>
  <a class="abs cat-btn cat-glass">GLASS</a>
  <a class="abs cat-btn cat-solid">SOLID<br>SURFACES</a>
</section>

<section>
  <div class="abs stack-back" role="img" aria-label="Project photo of a kitchen interior"></div>
  <div class="abs stack-mid" role="img" aria-label="Project photo of a white bathroom with freestanding bath"></div>
  <div class="abs stack-front" role="img" aria-label="Solid surface shower tray with round drain"></div>
  <a class="abs pager pager-prev"><svg width="12" height="16" viewBox="0 0 12 16"><polyline points="9,2 3,8 9,14" fill="none" stroke="#1b8a9b" stroke-width="2"/></svg></a>
  <a class="abs pager pager-next"><svg width="12" height="16" viewBox="0 0 12 16"><polyline points="3,2 9,8 3,14" fill="none" stroke="#fff" stroke-width="2"/></svg></a>
  <h2 class="abs feature-title">VELMARA</h2>
  <h3 class="abs feature-sub">made to measure</h3>
  <p class="abs feature-text">Solid surface Velmara is well known as one of the most versatile and resilient options for kitchens and bathrooms, and it is now being used extensively in the leisure and hospitality industry in lobbies, bars and restaurants. At Brightwell Pane Splashes, we manufacture our own in-house, and can create any shape and size of Velmara for your project. It is completely seamless, so large spaces can be covered with no interruption to the smooth lines. Velmara is non-porous and heat-resistant, so perfect for busy areas.</p>
  <a class="abs btn-more">View More</a>
</section>

<section>
  <div class="abs about"></div>
  <h2 class="abs about-title office-title">Our Virtual Office!</h2>
  <div class="abs office-text">
    <p>We are proud to have a virtual office at the St Aldric's Innovation Centre in the heart of Cambridge.&nbsp; It is important for us to have a presence in this vital city and this particular centre is second to none.</p>
    <p>If you are interested in learning more about our business, either as a client or supplier, then please do <a>get in touch</a>.</p>
  </div>
  <div class="abs office-photo" role="img" aria-label="Innovation centre building among trees"></div>
  <div class="abs map" role="img" aria-label="Map of the United Kingdom by nation"></div>
  <h2 class="abs about-title coverage-title">Nationalwide Coverage</h2>
  <div class="abs coverage-text">
    <p>Part of the prestigious University of Wexmoor, St Aldric's Innovation Centre has been granted full membership of the Continental Enterprise Hub Network (CEHN), which is extremely reassuring for our clients that travel from abroad.</p>
    <p>It was also the first accredited “BIC” (Business and Innovation Centre) in the<br>East of England.</p>
  </div>
</section>

<footer class="abs footer"></footer>
<div class="abs foot-label follow-label">FOLLOW US</div>
<div class="abs social"><span class="s1"></span><span class="s2"></span><span class="s3"></span><span class="s4"></span></div>
<div class="abs follow-rule"></div>
<div class="abs legal">Privacy<span class="sep">|</span>Terms and Conditions</div>
<div class="abs foot-divider"></div>
<div class="abs foot-label contact-label">CONTACT US</div>
<div class="abs contact-row row-phone">
  <svg width="26" height="24" viewBox="0 0 26 24"><path d="M6 2 L10 7 L8 10 Q11 15 16 17 L19 14 L24 18 L21 22 Q10 22 3 8 Z" fill="none" stroke="#333" stroke-width="1.5" stroke-linejoin="round"/></svg>
  <span>+44 (0)1632 960 548</span>
</div>
<div class="abs contact-row row-mail">
  <svg width="26" height="18" viewBox="0 0 26 18"><rect x="1" y="1" width="24" height="16" fill="none" stroke="#333" stroke-width="1.5"/><polyline points="1,1 13,10 25,1" fill="none" stroke="#333" stroke-width="1.5"/></svg>
  <span>sales@brightwellpanesplashes.co.uk</span>
</div>
<div class="abs copyright">Copyrights @ 2018 brightwellps.com</div>
<div class="abs foot-brand"><span class="dot"></span>Brightwell Panes &amp; Stoneworks</div>

</body>
</html>
```